Ridgecrest Capital Allies need a desert themed website!

We need a web design and development for our informational website for our new company named Ridgecrest Capital Allies. We would like it to be desert themed and it can be color or black and white. We would like it to be classy and clean, while also talking to the benefits of investment partner with us.

We're thinking probably a home page with a nice image of a Scottsdale landscape, then other pages would What we offer our partners page (or other wording if you find something better), a meet the founder page, and a contact us page.

What we offer our partners (or other wording if you think of something better):
Our investors offer an opportunity to families that cannot usually get approved for a mortgage, to be able to become future homeowners. Thus, Benefiting both the investors and local surrounding community members. Our investors get to both have all the benefits of an investment with receiving above market rates of return to themselves and helping families find homes at the same time.

Maybe also build an infographic with these benefits: Safety, Security, Long-term investment horizon, cashflow, tax benefits, above market rate of return, and capital growth.

And a meet the founder page. With my headshot.

Paul Harnetti is a private equity investor providing significantly above market returns to his investment partners while taking the time to be involved with his community and family. Paul first honed his skills in taking calculated risk decisions while very young where he took on playing poker professionally. He succeeded at the highest levels for over a decade competing in high stakes professional cash games around the world.

From the poker world he transitioned to investing in public and private markets. He took an approach of knowing the companies he invests in intimately and after over 10,000 hours of research became known in his community as the person to get investment advice on the electric vehicle industry for his voracious research and expert insight.

He now invests in single family homes in the Phoenix market using his past experience analyzing probabilistic outcomes and comparing the ROIs of different potential strategies. These skills have contributed to his success in investing in companies where he used his ability to assess risk to reward ratios to significantly outperform the market over an extended period.

Contact page we want my email Paul@RidgecrestFunds.example, my instagram: @PaulHarnetti, and my linkedin https://www.profilehub.example/in/paul-harnetti-58172036/

I have included my headshot for the about me page. I've included some saguaro generated images feel free to incorporate into the website (or make them the company logo), or not, whatever you feel gives the best look for the website.

```html
<!DOCTYPE html>
<html lang="en">
<head>
<meta charset="utf-8">
<title>Ridgecrest Capital Allies</title>
<link rel="stylesheet" href="https://fonts.googleapis.com/css2?family=Montserrat:wght@400;500;600;700&family=Roboto+Condensed:wght@700&display=swap">
<style>
:root{
  --orange:#e0985a;
  --orange-dark:#d98a45;
  --teal:#234d5c;
  --maroon:#8a3a2a;
  --navy:#1f4a78;
  --ink:#2b2b2b;
  --muted:#444;
  --gray-bg:#f5f5f5;
  --beige:#f8e8da;
  --white:#fff;
  --line:#d8d8d8;
}
*{box-sizing:border-box;margin:0;padding:0}
html,body{width:1200px;height:3849px;overflow:hidden}
body{position:relative;background:var(--white);font-family:"Montserrat",sans-serif;color:var(--ink)}
.abs{position:absolute}

/* hero */
.hero{left:0;top:0;width:1200px;height:604px;
  clip-path:polygon(0 0,100% 0,100% 508px,0 600px);
  background:linear-gradient(180deg,#2f7fd6 0%,#6aa7e0 32%,#a7b9c9 50%,#8c7d6e 70%,#5e4a38 100%)}
.hero-rule{left:0;top:500px}
.brand{display:flex;align-items:center;gap:14px}
.brand-mark{width:75px;height:75px;border-radius:50%;background:var(--orange);border:3px solid rgba(255,255,255,.8)}
.brand-name{font-family:"Roboto Condensed",sans-serif;font-weight:700;color:var(--white);line-height:1}
.brand-name span{display:block}
.hero .brand{left:100px;top:18px}
.hero .brand-name{font-size:36px}
.hero .brand-name span+span{font-size:20px;margin-top:2px}
.btn{display:flex;align-items:center;justify-content:center;font-family:"Montserrat",sans-serif;font-weight:600;color:var(--white);text-decoration:none}
.btn-teal{background:var(--teal)}
.btn-orange{background:var(--orange)}
.hero-nav-btn{left:976px;top:22px;width:122px;height:46px;font-size:16px;border-radius:3px}
.hero-title{left:98px;top:172px;font-family:"Roboto Condensed",sans-serif;font-weight:700;font-size:60px;line-height:62px;color:var(--white)}
.hero-sub{left:98px;top:300px;font-weight:700;font-size:18px;line-height:26px;color:var(--white);width:560px}
.hero-btn{left:97px;top:368px;width:120px;height:46px;font-size:16px}

/* offer */
.offer-dot{left:97px;top:640px;width:117px;height:117px;border-radius:50%;background:var(--beige)}
.offer-photo{left:155px;top:692px;width:517px;height:585px;border-radius:6px;
  background:linear-gradient(150deg,#1b2330 0%,#3a4658 45%,#6d7b8e 70%,#2a3342 100%)}
.offer-card{left:612px;top:728px;width:437px;height:508px;background:var(--white);box-shadow:0 2px 18px rgba(0,0,0,.08);padding:58px 22px 0 30px}
.section-title{font-family:"Montserrat",sans-serif;font-weight:500;color:var(--maroon);font-size:29px}
.offer-card .section-title{font-size:25.5px;white-space:nowrap;letter-spacing:-.2px}
.title-rule{display:flex;gap:6px;margin:6px 0 0}
.title-rule i{display:block;width:38px;height:3px}
.title-rule i:first-child{background:var(--teal)}
.title-rule i:last-child{background:var(--orange)}
.offer-card p{font-size:13px;line-height:28px;color:var(--muted);margin-top:12px;max-width:380px}
.offer-card p+p{margin-top:3px}
.offer-card .btn{width:120px;height:48px;font-size:15px;margin-top:22px;margin-left:-3px}

/* benefits */
.benefits{left:0;top:1380px;width:1200px;height:764px;background:var(--gray-bg)}
.eyebrow{left:154px;top:1493px;font-weight:600;font-size:20px;color:var(--navy)}
.benefits-title{left:153px;top:1518px;font-weight:600;font-size:38px;color:var(--maroon)}
.benefits-btn{left:819px;top:1496px;width:242px;height:64px;font-size:19px;font-weight:500;gap:12px}
.band{left:97px;top:1720px;width:1003px;height:321px;background:var(--orange)}
.tile{width:216px;height:173px;background:var(--white);padding:22px 18px;border-radius:2px}
.tile-icon{width:64px;height:64px;border-radius:50%;background:var(--beige);display:flex;align-items:center;justify-content:center}
.tile-label{font-size:14px;line-height:21px;color:var(--ink);margin-top:12px}
.cactus-disc{left:876px;top:1824px;width:164px;height:164px;border-radius:50%;border:4px solid var(--white);
  background:linear-gradient(180deg,#e3c8a8 0%,#d9a478 45%,#9b7a4e 70%,#5e6b3a 100%)}

/* about */
.about-title{left:0;top:2236px;width:1200px;text-align:center;font-weight:500;font-size:29px;color:var(--maroon)}
.about-title small{font-size:23px}
.about-rule{left:555px;top:2285px}
.about-intro{left:130px;top:2305px;width:940px;text-align:center;font-size:13.5px;line-height:27.6px;color:var(--muted)}
.about-intro b,.about-body b{font-weight:700;color:var(--ink)}
.about-body{left:99px;top:2462px;width:495px;font-size:13.5px;line-height:27.8px;color:var(--muted)}
.about-body p+p{margin-top:14px}
.about-photo{left:641px;top:2446px;width:457px;height:448px;border:2px solid var(--orange);border-radius:4px;
  background:linear-gradient(160deg,#d8c6a6 0%,#c9b08a 50%,#a88a66 100%)}
.mail-btn{left:97px;top:2804px;min-width:344px;height:65px;background:var(--teal);display:flex;align-items:center;gap:14px;padding:0 20px 0 18px;color:var(--white);white-space:nowrap}
.mail-btn small{display:block;font-size:11.5px}
.mail-btn strong{display:block;font-weight:500;font-size:18px}

/* footer */
.footer{left:0;top:3380px;width:1200px;height:469px;
  clip-path:polygon(0 83px,100% 0,100% 100%,0 100%);
  background:linear-gradient(180deg,#3a2a22 0%,#2b2a33 40%,#1e2a3a 100%)}
.footer-rule{left:0;top:3376px}
.footer .brand{left:395px;top:196px}
.footer .brand-mark{width:88px;height:88px}
.footer .brand-name{font-size:48px}
.footer .brand-name span+span{font-size:23px;margin-top:4px}
.info{display:flex;align-items:center;gap:10px;color:var(--white);font-size:12.5px;line-height:19px;font-weight:500}
.copyright{left:0;top:3806px;width:1200px;text-align:center;color:var(--white);font-size:13.5px}

/* contact */
.contact-card{left:182px;top:2997px;width:840px;height:511px;background:var(--white);box-shadow:0 2px 18px rgba(0,0,0,.08);
  clip-path:polygon(0 0,100% 0,100% 460px,790px 100%,0 100%)}
.fold{left:976px;top:3457px}
.contact-title{left:182px;top:3030px;width:840px;text-align:center;font-weight:500;font-size:29px;color:var(--maroon)}
.contact-rule{left:555px;top:3078px}
.contact-lead{left:182px;top:3096px;width:840px;text-align:center;font-size:15.5px;color:var(--ink)}
.field{height:42px;border:1px solid var(--line);display:flex;align-items:center;gap:14px;padding-left:14px;font-size:12.5px;color:#555;background:var(--white)}
.field.msg{height:101px;align-items:flex-start;padding-top:12px}
.send-btn{left:523px;top:3394px;width:154px;height:44px;font-size:15px;border-radius:3px}
</style>
</head>
<body>

<!-- Hero -->
<section class="hero abs" role="img" aria-label="Desert city skyline with mountains and a tall saguaro cactus under a blue sky">
  <div class="brand abs">
    <span class="brand-mark"></span>
    <span class="brand-name"><span>Ridgecrest</span><span>Capital Allies</span></span>
  </div>
  <a class="btn btn-teal hero-nav-btn abs" href="#contact">Contact Us</a>
  <h1 class="hero-title abs">Strength In Partnership,<br>Growth In Investment.</h1>
  <p class="hero-sub abs">We Help Our Investors Invest In Real Estate For Safe And Secure Long-term Cash Flow.</p>
  <a class="btn btn-orange hero-btn abs" href="#contact">Contact Us</a>
</section>
<svg class="hero-rule abs" width="1200" height="110" viewBox="0 0 1200 110"><line x1="0" y1="102" x2="1200" y2="8" stroke="#e0985a" stroke-width="5"/></svg>

<!-- What we offer -->
<div class="offer-dot abs"></div>
<div class="offer-photo abs" role="img" aria-label="Hand drawing a glowing house and rising growth arrow"></div>
<article class="offer-card abs">
  <h2 class="section-title">What We Offer Our Partners</h2>
  <div class="title-rule"><i></i><i></i></div>
  <p>Our investors offer an opportunity to families that cannot usually get approved for a mortgage, to be able to become future homeowners. Thus, Benefiting both the investors and local surrounding community members.</p>
  <p>Our investors get to both have all the benefits of an investment with receiving above market rates of return to themselves and helping families find homes at the same time.</p>
  <a class="btn btn-orange" href="#contact">Contact Us</a>
</article>

<!-- Benefits -->
<section class="benefits abs"></section>
<p class="eyebrow abs">Benefits</p>
<h2 class="benefits-title abs">Why Invest With Us</h2>
<a class="btn btn-teal benefits-btn abs" href="#contact">
  <svg width="28" height="28" viewBox="0 0 24 24" fill="none" stroke="#fff" stroke-width="1.4"><path d="M5 3h4l2 5-3 2a11 11 0 0 0 6 6l2-3 5 2v4a2 2 0 0 1-2 2A17 17 0 0 1 3 5a2 2 0 0 1 2-2z"/><path d="M15 3a6 6 0 0 1 6 6M15 7a2 2 0 0 1 2 2"/></svg>
  Contact Us Today
</a>
<div class="band abs"></div>

<div class="tile abs" style="left:134px;top:1605px">
  <div class="tile-icon"><svg width="34" height="34" viewBox="0 0 24 24" fill="none" stroke="#234d5c" stroke-width="1.3"><path d="M12 3l8 4v5c0 5-4 8-8 9-4-1-8-4-8-9V7z"/><path d="M12 8v8M10 10h3a1.5 1.5 0 0 1 0 3h-2a1.5 1.5 0 0 0 0 3h3"/></svg></div>
  <p class="tile-label">Safety</p>
</div>
<div class="tile abs" style="left:375px;top:1605px">
  <div class="tile-icon"><svg width="34" height="34" viewBox="0 0 24 24" fill="none" stroke="#234d5c" stroke-width="1.3"><path d="M12 3l8 4v5c0 5-4 8-8 9-4-1-8-4-8-9V7z"/><rect x="9" y="11" width="6" height="5"/><path d="M10 11V9a2 2 0 0 1 4 0v2"/></svg></div>
  <p class="tile-label">Security</p>
</div>
<div class="tile abs" style="left:611px;top:1605px">
  <div class="tile-icon"><svg width="34" height="34" viewBox="0 0 24 24" fill="none" stroke="#234d5c" stroke-width="1.3"><path d="M11 3l7 3v5c0 4-3 7-7 8-4-1-7-4-7-8V6z"/><path d="M8 11l2 2 4-4"/><circle cx="18" cy="18" r="3.5"/></svg></div>
  <p class="tile-label">Long-term Investment<br>Horizon</p>
</div>
<div class="tile abs" style="left:849px;top:1605px">
  <div class="tile-icon"><svg width="34" height="34" viewBox="0 0 24 24" fill="none" stroke="#234d5c" stroke-width="1.3"><rect x="3" y="8" width="14" height="8" rx="1" transform="rotate(-20 10 12)"/><circle cx="10" cy="12" r="2.2"/><path d="M18 14l3 2M3 10l-1-1"/></svg></div>
  <p class="tile-label">Cashflow</p>
</div>
<div class="tile abs" style="left:134px;top:1823px">
  <div class="tile-icon"><svg width="34" height="34" viewBox="0 0 24 24" fill="none" stroke="#234d5c" stroke-width="1.3"><path d="M5 3h10v18H5z"/><path d="M8 7h4M8 10h4M8 13h3"/><circle cx="17" cy="17" r="4"/><path d="M15.5 18.5l3-3"/></svg></div>
  <p class="tile-label">Tax Benefits</p>
</div>
<div class="tile abs" style="left:375px;top:1823px">
  <div class="tile-icon"><svg width="34" height="34" viewBox="0 0 24 24" fill="none" stroke="#234d5c" stroke-width="1.3"><path d="M3 17l5-2 6 2 6-3v3l-6 3-6-2-5 1z"/><circle cx="9" cy="7" r="2"/><circle cx="15" cy="5" r="2"/><path d="M12 14V9"/></svg></div>
  <p class="tile-label">Above<br>Market Rate of Return</p>
</div>
<div class="tile abs" style="left:611px;top:1823px">
  <div class="tile-icon"><svg width="34" height="34" viewBox="0 0 24 24" fill="none" stroke="#234d5c" stroke-width="1.3"><path d="M3 3v18h18"/><path d="M7 17v-3M11 17v-5M15 17v-7M19 17V8"/><circle cx="9" cy="6" r="2.5"/></svg></div>
  <p class="tile-label">Capital Growth</p>
</div>
<div class="cactus-disc abs" role="img" aria-label="Saguaro cactus in a desert at sunset"></div>

<!-- About -->
<h2 class="about-title abs">About Paul Harnetti,<small>Founder</small></h2>
<div class="title-rule about-rule abs"><i></i><i></i></div>
<p class="about-intro abs"><b>Paul Harnetti is a private equity investor</b> providing significantly above market returns to his investment partners while taking the time to be involved with his community and family. Paul first honed his skills in taking calculated risk decisions while very young where he took on playing poker professionally. He succeeded at the highest levels for over a decade competing in high stakes professional cash games around the world</p>
<div class="about-body abs">
  <p>From the poker world he transitioned to investing in public and private markets. He took an approach of knowing the companies he invests in intimately and after over 10,000 hours of research became known in his community as the person to get investment advice on the electric vehicle industry for his voracious research and expert insight.</p>
  <p>He now <b>invests in single family homes in the Phoenix market</b> using his past experience analyzing probabilistic outcomes &amp; comparing the ROIs of different potential strategies. These skills have contributed to his success in investing in companies where he used his ability to assess risk to reward ratios to significantly outperform the market over an extended period.</p>
</div>
<div class="about-photo abs" role="img" aria-label="Headshot of founder Paul Harnetti"></div>
<a class="mail-btn abs" href="mailto:Paul@RidgecrestFunds.example" style="text-decoration:none">
  <svg width="32" height="32" viewBox="0 0 24 24" fill="none" stroke="#fff" stroke-width="1.2"><path d="M3 10l9-6 9 6v10H3z"/><path d="M3 10l9 6 9-6"/><rect x="7" y="6" width="10" height="6"/></svg>
  <span><small>Contact Me Today</small><strong>Paul@RidgecrestFunds.example</strong></span>
</a>

<!-- Footer -->
<footer class="footer abs" role="img" aria-label="Desert city skyline at dusk">
  <div class="brand abs">
    <span class="brand-mark"></span>
    <span class="brand-name"><span>Ridgecrest</span><span>Capital Allies</span></span>
  </div>
  <div class="info abs" style="left:143px;top:323px">
    <svg width="26" height="30" viewBox="0 0 24 28" fill="none" stroke="#e0985a" stroke-width="1.5"><path d="M12 26s-8-9-8-15a8 8 0 0 1 16 0c0 6-8 15-8 15z"/><circle cx="12" cy="11" r="3"/></svg>
    <span>Address<br>Ridgecrest Mesa, Arizona, United States</span>
  </div>
  <div class="info abs" style="left:449px;top:323px">
    <svg width="30" height="30" viewBox="0 0 24 24" fill="none" stroke="#e0985a" stroke-width="1.4"><path d="M5 3h4l2 5-3 2a11 11 0 0 0 6 6l2-3 5 2v4a2 2 0 0 1-2 2A17 17 0 0 1 3 5a2 2 0 0 1 2-2z"/></svg>
    <span>Phone<br>555.014.2290</span>
  </div>
  <div class="info abs" style="left:629px;top:323px">
    <svg width="28" height="28" viewBox="0 0 24 24" fill="none" stroke="#e0985a" stroke-width="1.4"><rect x="3" y="6" width="18" height="13"/><path d="M3 6l9 7 9-7"/></svg>
    <span>Email<br>paul@ridgecrestfunds.example</span>
  </div>
  <div class="info abs" style="left:907px;top:323px">
    <svg width="26" height="30" viewBox="0 0 24 28" fill="none" stroke="#e0985a" stroke-width="1.5"><path d="M12 26s-8-9-8-15a8 8 0 0 1 16 0c0 6-8 15-8 15z"/><circle cx="12" cy="11" r="3"/></svg>
    <span>Location Map<br><u>View Directions</u></span>
  </div>
</footer>
<svg class="footer-rule abs" width="1200" height="92" viewBox="0 0 1200 92"><line x1="0" y1="88" x2="1200" y2="4" stroke="#e0985a" stroke-width="5"/></svg>
<p class="copyright abs">©2024. Ridgecrest Capital Allies. All Rights Reserved</p>

<!-- Contact -->
<section id="contact" class="contact-card abs"></section>
<svg class="fold abs" width="46" height="46" viewBox="0 0 46 46"><polygon points="0,0 46,0 0,46" fill="#e0985a"/></svg>
<h2 class="contact-title abs">Contact Me Today</h2>
<div class="title-rule contact-rule abs"><i></i><i></i></div>
<p class="contact-lead abs">Feel Free To Reach Out To Me Today For Any Inquiries Or To Discuss Further!</p>
<div class="field abs" style="left:257px;top:3152px;width:333px">
  <svg width="16" height="16" viewBox="0 0 24 24" fill="none" stroke="#234d5c" stroke-width="1.5"><circle cx="12" cy="8" r="4"/><path d="M4 21c0-4 4-6 8-6s8 2 8 6z"/></svg>First Name</div>
<div class="field abs" style="left:608px;top:3152px;width:333px">
  <svg width="16" height="16" viewBox="0 0 24 24" fill="none" stroke="#234d5c" stroke-width="1.5"><circle cx="12" cy="8" r="4"/><path d="M4 21c0-4 4-6 8-6s8 2 8 6z"/></svg>Last Name</div>
<div class="field abs" style="left:257px;top:3212px;width:333px">
  <svg width="18" height="16" viewBox="0 0 24 20" fill="none" stroke="#234d5c" stroke-width="1.5"><rect x="2" y="2" width="20" height="16"/><path d="M2 2l10 8 10-8"/></svg>Email</div>
<div class="field abs" style="left:608px;top:3212px;width:333px">
  <svg width="18" height="18" viewBox="0 0 24 24" fill="none" stroke="#234d5c" stroke-width="1.5"><path d="M5 3h4l2 5-3 2a11 11 0 0 0 6 6l2-3 5 2v4a2 2 0 0 1-2 2A17 17 0 0 1 3 5a2 2 0 0 1 2-2z"/></svg>Phone</div>
<div class="field msg abs" style="left:257px;top:3272px;width:684px">
  <svg width="18" height="18" viewBox="0 0 24 24" fill="none" stroke="#234d5c" stroke-width="1.5"><path d="M3 4h18v12H9l-5 4v-4H3z"/><path d="M7 8h10M7 12h6"/></svg>Message</div>
<a class="btn btn-teal send-btn abs" href="#contact">Send Message</a>

</body>
</html>
```